Retractable Banners Designs for Tradeshows

We like the look and feel of the banners draft but want a more polished and improved version of the banners

The dimensions of each banner should be 33" x 80"

We want the banners to work on their own as they will be used in different places, but at tradeshows, they might be used side by side in a 10x10 tradeshow booth, so common design elements that work together is needed.
Updates

Low design quality

Target Market(s)

tradeshows booths

Colors
EB3D1F
EC4F4E
F09395
F8D3D4
FCEDEE

Requirements
Must have
• Elements that tie all the banners together, large scale images, not to cluttered or busy, designed to be visible and attractive from far away, our corporate colours are red, black, white and gray
Nice to have
• bright design not dark but using our corporate colours of red, gray, white and some black

```html
<!DOCTYPE html>
<html lang="en">
<head>
<meta charset="utf-8">
<title>Tradeshow Banner Series</title>
<link href="https://fonts.googleapis.com/css2?family=Open+Sans:wght@400;600;700&display=swap" rel="stylesheet">
<style>
  :root {
    --stage: #616161;
    --red: #e2232b;
    --white: #ffffff;
    --sky-deep: #1f3594;
    --sky-light: #6f8fdc;
    --steel-dark: #1e2633;
    --steel-mid: #4a5a72;
    --steel-light: #a9b4c4;
    --lab-dark: #1c1c1c;
    --lab-mid: #6b6b68;
    --lab-light: #c4c4c0;
    --field-dark: #3e4250;
    --field-mid: #8c909c;
    --field-light: #c9ccd2;
    --field-warm: #9a5a55;
  }
  * { margin: 0; padding: 0; box-sizing: border-box; }
  html, body {
    width: 800px; height: 1200px; overflow: hidden;
    background: var(--stage);
    font-family: "Open Sans", Arial, sans-serif;
  }
  .banner-row {
    position: absolute;
    left: 40px; top: 382px;
    width: 720px; height: 436px;
    display: flex;
  }
  .banner {
    position: relative;
    width: 180px; height: 436px;
    overflow: hidden;
  }
  .banner-photo { position: absolute; inset: 0; }
  .photo-towers {
    background:
      radial-gradient(ellipse 70% 40% at 60% 70%, rgba(240,240,245,0.55), transparent 70%),
      radial-gradient(ellipse 90% 35% at 40% 95%, rgba(20,22,30,0.9), transparent 75%),
      linear-gradient(180deg, var(--sky-deep) 0%, #3556c0 35%, var(--sky-light) 75%, #4a5478 100%);
  }
  .photo-racks {
    background:
      radial-gradient(ellipse 45% 60% at 55% 40%, rgba(190,205,225,0.45), transparent 70%),
      radial-gradient(ellipse 30% 80% at 12% 50%, rgba(10,14,22,0.7), transparent 75%),
      linear-gradient(170deg, var(--steel-mid) 0%, var(--steel-dark) 40%, var(--steel-mid) 70%, var(--steel-light) 100%);
  }
  .photo-lab {
    background:
      radial-gradient(ellipse 80% 18% at 50% 36%, rgba(235,235,230,0.6), transparent 75%),
      radial-gradient(ellipse 70% 25% at 45% 72%, rgba(40,40,42,0.9), transparent 75%),
      linear-gradient(180deg, var(--lab-dark) 0%, var(--lab-light) 28%, var(--lab-mid) 48%, var(--lab-light) 60%, var(--lab-dark) 100%);
  }
  .photo-field {
    background:
      radial-gradient(ellipse 40% 30% at 30% 45%, rgba(225,228,232,0.6), transparent 75%),
      radial-gradient(ellipse 45% 60% at 85% 45%, rgba(160,80,75,0.55), transparent 75%),
      linear-gradient(165deg, var(--field-dark) 0%, var(--field-mid) 35%, var(--field-light) 60%, var(--field-warm) 100%);
  }
  .brand-name {
    position: absolute;
    top: 34px; left: 0; right: 0;
    text-align: center;
    color: var(--white);
    font-weight: 400;
    font-size: 18px;
  }
  .info-panel {
    position: absolute;
    left: 12px; top: 283px;
    width: 155px; height: 141px;
    background: var(--red);
    opacity: 0.95;
    padding: 9px 8px 0 9px;
    color: var(--white);
  }
  .panel-title {
    font-weight: 700;
    font-size: 15px;
    line-height: 18px;
    height: 36px;
    text-transform: uppercase;
    white-space: nowrap;
  }
  .panel-title.single { padding-top: 18px; }
  .panel-rule {
    width: 32px; height: 2px;
    background: var(--white);
    margin: 10px 0 9px 1px;
  }
  .panel-text {
    font-weight: 400;
    font-size: 12px;
    line-height: 14.2px;
    white-space: nowrap;
  }
</style>
</head>
<body>
  <main class="banner-row">
    <section class="banner">
      <div class="banner-photo photo-towers" role="img" aria-label="Cellular antenna tower against a blue sky"></div>
      <div class="brand-name">relaywave</div>
      <div class="info-panel">
        <h2 class="panel-title">Telecom<br>Infrastructure</h2>
        <div class="panel-rule"></div>
        <p class="panel-text">Cutting edge solutions<br>for the Next Generation</p>
      </div>
    </section>
    <section class="banner">
      <div class="banner-photo photo-racks" role="img" aria-label="Server racks in a data centre"></div>
      <div class="brand-name">relaywave</div>
      <div class="info-panel">
        <h2 class="panel-title">ICT<br>Solutions</h2>
        <div class="panel-rule"></div>
        <p class="panel-text">Seamless Cable and<br>Telecom Networks and<br>Enterprise Deployments</p>
      </div>
    </section>
    <section class="banner">
      <div class="banner-photo photo-lab" role="img" aria-label="Electronic test and measurement instruments on shelves"></div>
      <div class="brand-name">relaywave</div>
      <div class="info-panel">
        <h2 class="panel-title">Test &amp;<br>Measurements</h2>
        <div class="panel-rule"></div>
        <p class="panel-text">Accurate and Efficient<br>Solutions for the<br>Wireless World</p>
      </div>
    </section>
    <section class="banner">
      <div class="banner-photo photo-field" role="img" aria-label="Technician in a hard hat installing radio hardware"></div>
      <div class="brand-name">relaywave</div>
      <div class="info-panel">
        <h2 class="panel-title single">Hardware</h2>
        <div class="panel-rule"></div>
        <p class="panel-text">High-Quality<br>Economical, Test Grade<br>RF and Microwave<br>Components</p>
      </div>
    </section>
  </main>
</body>
</html>
```